Business Card Design

We need a business card design for a new company called Riverbend Advisory, LLC. We are a project management and software engineering consulting company. We prefer to use blues but am open to any colors. We would like out design to show strength and creativity.
Updates

I've uploaded new logo designs to the project.  Please use these logo designs for the business card. Thanks!

Industry/Entity Type

Software

Contact Information for Business Card

Harold Whitcombe
Consultant
Owner

Riverbend Advisory, LLC

2750 5th Ave. S #3274
Arlington, VA 22917

703-555-0186
hwhitcombe@rvbdax.example
www.rvbdax.example

```html
<!DOCTYPE html>
<html lang="en">
<head>
<meta charset="utf-8">
<title>Riverbend Advisory – Business Card</title>
<link rel="stylesheet" href="https://fonts.googleapis.com/css2?family=Oswald:wght@500&family=Share+Tech+Mono&display=swap">
<style>
  :root {
    --page-bg: #2b2b2b;
    --card-bg: #f1f1f1;
    --brand-blue: #1f6f8b;
    --ink: #3d3d3d;
    --ink-soft: #4a4a4a;
    --art-tone: #5a5a5a;
  }
  * { margin: 0; padding: 0; box-sizing: border-box; }
  html, body {
    width: 1166px;
    height: 1200px;
    overflow: hidden;
    background: var(--page-bg);
  }
  .card {
    position: absolute;
    left: 133px;
    top: 340px;
    width: 900px;
    height: 520px;
    background: var(--card-bg);
    color: var(--ink);
    font-family: "Share Tech Mono", monospace;
  }
  .monitor-icon {
    position: absolute;
    left: 110px;
    top: 150px;
    width: 100px;
    height: 90px;
  }
  .brand-name {
    position: absolute;
    left: 290px;
    top: 120px;
    width: 320px;
    text-align: center;
    font-family: "Oswald", sans-serif;
    font-weight: 500;
    font-size: 30px;
    letter-spacing: 2px;
    color: var(--brand-blue);
    text-transform: uppercase;
  }
  .head-illustration {
    position: absolute;
    left: 680px;
    top: 70px;
    width: 90px;
    height: 95px;
    border-radius: 45% 50% 40% 45%;
    background: radial-gradient(circle at 45% 45%, #777 0%, var(--art-tone) 70%);
  }
  .person-name {
    position: absolute;
    left: 230px;
    top: 225px;
    width: 440px;
    text-align: center;
    font-family: "Oswald", sans-serif;
    font-weight: 500;
    font-size: 40px;
    letter-spacing: 1px;
    color: var(--brand-blue);
    text-transform: uppercase;
  }
  .person-role {
    position: absolute;
    left: 180px;
    top: 285px;
    width: 560px;
    text-align: center;
    font-size: 17px;
    letter-spacing: 2px;
    text-transform: uppercase;
    color: var(--ink-soft);
  }
  .contact-online {
    position: absolute;
    right: 50px;
    top: 330px;
    text-align: right;
    font-size: 15px;
    line-height: 1.5;
    text-transform: uppercase;
  }
  .contact-address {
    position: absolute;
    left: 70px;
    top: 400px;
    font-size: 17px;
    line-height: 1.5;
    letter-spacing: 1px;
    text-transform: uppercase;
  }
</style>
</head>
<body>
  <article class="card">
    <svg class="monitor-icon" viewBox="0 0 100 90" aria-hidden="true">
      <rect x="6" y="4" width="88" height="62" rx="10" fill="none" stroke="#3d3d3d" stroke-width="8"/>
      <circle cx="82" cy="55" r="3" fill="#3d3d3d"/>
      <rect x="44" y="66" width="12" height="12" fill="#3d3d3d"/>
      <rect x="24" y="78" width="52" height="7" rx="2" fill="#3d3d3d"/>
    </svg>

    <div class="brand-name">Riverbend Advisory</div>

    <div class="head-illustration" role="img" aria-label="Illustration of a head filled with gears and tools, in dark grey"></div>

    <h1 class="person-name">Harold Whitcombe</h1>
    <p class="person-role">Consultant Owner Riverbend Advisory</p>

    <p class="contact-online">hwhitcombe@rvbdax.example<br>www.rvbdax.example</p>

    <p class="contact-address">LLC 2750 5th Ave. S #3274 Arlington<br>VA 22917 703-555-0186</p>
  </article>
</body>
</html>
```